Northern Terrain Published Photographer Website

I need a website to feature a home page slide show of 6 of my top photos then a few simple pages including; gallery, bio, social, checkout, services
Updates

Need extra days to review

Target Market(s)

photography

Industry/Entity Type

Photographer

Coding

Coded - Design and coding required

Number of Pages Required

5+ page

Colors

Designer to choose colors to be used in the design.

Requirements
Must have
• clean eye catching elegant trendy
Nice to have
• unique and creative from other photographer websites

```html
<!DOCTYPE html>
<html lang="en">
<head>
<meta charset="utf-8">
<title>Northern Terrain Photography – About</title>
<link rel="stylesheet" href="https://fonts.googleapis.com/css2?family=Jost:wght@400;500;600&family=Open+Sans:wght@400;600&display=swap">
<style>
  :root {
    --ink: #000000;
    --sidebar: #121212;
    --road-dark: #0c0c0c;
    --road-mid: #333333;
    --text: #ffffff;
    --muted: #9a9a9a;
    --accent: #e41b4f;
    --portrait-top: #7d6a45;
    --portrait-bottom: #4e4e4e;
  }
  * { box-sizing: border-box; margin: 0; padding: 0; }
  html, body { width: 1200px; height: 613px; overflow: hidden; background: var(--ink); }
  .canvas {
    position: relative; width: 1200px; height: 613px; overflow: hidden;
    background: var(--ink); color: var(--text);
    font-family: "Jost", "Futura", sans-serif;
  }

  /* Sidebar */
  .sidebar { position: absolute; left: 0; top: 0; width: 270px; height: 613px; background: var(--sidebar); }
  .sidebar-photo {
    position: absolute; left: 0; top: 270px; width: 270px; height: 343px;
    background: linear-gradient(160deg, var(--sidebar) 0%, var(--road-mid) 55%, var(--road-dark) 100%);
  }
  .brand {
    position: absolute; left: 20px; top: 36px;
    display: flex; align-items: center; gap: 10px;
    font-family: "Jost", sans-serif; font-weight: 400; font-size: 21px; letter-spacing: 0.5px;
    color: var(--text);
  }
  .brand-dot { width: 12px; height: 12px; border: 1.5px solid var(--text); border-radius: 50%; }

  .main-nav { position: absolute; left: 20px; top: 207px; list-style: none; }
  .main-nav li {
    font-family: "Open Sans", sans-serif; font-size: 12.5px; letter-spacing: 0.2px;
    height: 40.3px; line-height: 20px; text-transform: uppercase;
  }
  .social { position: absolute; left: 20px; top: 412px; display: flex; gap: 8px; }
  .social span { width: 17px; height: 17px; border: 1.6px solid var(--text); border-radius: 50%; display: block; }

  .copyright {
    position: absolute; left: 20px; top: 570px;
    font-family: "Open Sans", sans-serif; font-size: 12px; text-transform: uppercase;
  }

  /* Content */
  .about { position: absolute; left: 330px; top: 129px; width: 372px; }
  .tag {
    display: inline-block; background: var(--accent); color: var(--text);
    font-weight: 600; font-size: 12px; letter-spacing: 0.3px;
    padding: 5px 8px; line-height: 17px; text-transform: uppercase;
  }
  .about h1 { font-weight: 400; font-size: 38px; line-height: 1; margin-top: 25px; }
  .about p { font-weight: 500; font-size: 14px; line-height: 20.6px; margin-top: 22px; }
  .read-more {
    display: inline-block; margin-top: 24px; width: 110px; height: 35px;
    border: 1px solid var(--text); text-align: center; line-height: 33px;
    font-size: 12px; text-transform: uppercase; color: var(--text); text-decoration: none;
  }
  .slider-arrows { position: absolute; left: 330px; top: 523px; display: flex; gap: 14px; }

  .portrait {
    position: absolute; left: 782px; top: 34px; width: 418px; height: 579px;
    background: linear-gradient(180deg, var(--portrait-top) 0%, var(--portrait-bottom) 100%);
  }
</style>
</head>
<body>
<div class="canvas">
  <aside class="sidebar">
    <div class="sidebar-photo" role="img" aria-label="Black and white photo of a winding road at night"></div>
    <div class="brand"><span>Northern Terrain</span><span class="brand-dot"></span></div>
    <ul class="main-nav">
      <li>Home</li>
      <li>Bio</li>
      <li>Services</li>
      <li>Gallery</li>
      <li>Checkout</li>
    </ul>
    <div class="social" aria-label="Social links">
      <span></span><span></span><span></span>
    </div>
    <div class="copyright">© 2019 Northern Terrain</div>
  </aside>

  <section class="about">
    <span class="tag">Photographer</span>
    <h1>About Maren</h1>
    <p>Lorem Ipsum is simply dummy text of the printing and typesetting industry. Lorem Ipsum has been the industry's standard dummy text ever since the 1500s, when an unknown printer took a galley of type and scrambled it to make a type specimen book. It has survived not only five centuries, but also the leap into electronic typesetting, remaining essentially unchanged.</p>
    <a class="read-more" href="#">Read More</a>
  </section>

  <div class="slider-arrows">
    <svg width="34" height="34" viewBox="0 0 34 34" aria-label="Previous">
      <circle cx="17" cy="17" r="15.5" fill="none" stroke="#9a9a9a" stroke-width="2"/>
      <polyline points="19.5,10 13,17 19.5,24" fill="none" stroke="#9a9a9a" stroke-width="2"/>
    </svg>
    <svg width="34" height="34" viewBox="0 0 34 34" aria-label="Next">
      <circle cx="17" cy="17" r="15.5" fill="none" stroke="#9a9a9a" stroke-width="2"/>
      <polyline points="14.5,10 21,17 14.5,24" fill="none" stroke="#9a9a9a" stroke-width="2"/>
    </svg>
  </div>

  <div class="portrait" role="img" aria-label="Portrait photo of the photographer"></div>
</div>
</body>
</html>
```